Telecommunications Company needs a business card design

We are looking for a sleek, professional and modern business card design based off our new logo. Will look at both light and dark options. On some designs please provide a small space for a QR code

Target Market(s)

B2B clients in Australia

Contact Information for Business Card

Name, Position, Brisbane (head) office, Phone number, email address, QR code (link to our website brightlinktelco.com.au

Colors
0054AA
0677BA
7BADD7
CADEEF
E8F1F8
0094D4
00A9DD
6FCCEA
C7EBF8
E9F6FB
00AB8E
00BBA5
67D7C9
C6EFE9
E9F9F6

```html
<!DOCTYPE html>
<html lang="en">
<head>
<meta charset="utf-8">
<title>Brightlink Telco – Business Card</title>
<link rel="stylesheet" href="https://fonts.googleapis.com/css2?family=Montserrat:wght@400;500;700&display=swap">
<style>
  :root{
    --bg:#d6d6d6;
    --white:#ffffff;
    --blue:#0677BA;
    --cyan:#00A9DD;
    --teal:#00AB8E;
    --teal-light:#00BBA5;
    --dark:#161618;
    --dark-2:#232326;
  }
  *{margin:0;padding:0;box-sizing:border-box}
  html,body{width:1200px;height:965px;overflow:hidden;background:var(--bg);font-family:"Montserrat",sans-serif}
  .stage{position:relative;width:1200px;height:965px}
  .card{position:absolute;top:114px;width:421px;height:736px;overflow:hidden}
  .card--front{left:141px;background:var(--white)}
  .card--back{left:638px;background:var(--dark)}

  .brand{position:absolute;left:0;right:0;top:104px;text-align:center;color:var(--blue);font-weight:700;line-height:1}
  .brand__name{display:block;font-size:54px;letter-spacing:.5px}
  .brand__sub{display:block;font-size:28px;letter-spacing:8px;margin-top:30px}

  .person{position:absolute;left:0;right:0;top:436px;text-align:center;line-height:1.2}
  .person__name{font-size:26px;font-weight:700;color:var(--blue);letter-spacing:.3px}
  .person__role{font-size:19px;font-weight:400;color:var(--cyan)}

  .divider{position:absolute;left:0;top:537px;width:421px;height:3px;background:var(--teal)}
  .contact-band{position:absolute;left:0;top:546px;width:421px;height:190px;
    background:linear-gradient(180deg,var(--blue) 0%,var(--teal-light) 100%)}
  .icons{position:absolute;left:0;top:520px;width:421px;height:40px}

  .contact{position:absolute;left:0;right:0;top:591px;text-align:center;color:var(--white);font-size:18.5px;line-height:25.5px;font-weight:400}

  .pattern{position:absolute;inset:0;background:linear-gradient(160deg,var(--dark-2) 0%,var(--dark) 55%,#0e0e10 100%)}
  .back-mark{position:absolute;left:180px;top:640px;width:150px;text-align:right;color:var(--teal-light);font-size:22px;font-weight:700;letter-spacing:.5px}
</style>
</head>
<body>
<main class="stage">
  <section class="card card--front">
    <div class="brand">
      <span class="brand__name">Brightlink</span>
      <span class="brand__sub">TELCO</span>
    </div>

    <div class="person">
      <p class="person__name">LIAM CARVER</p>
      <p class="person__role">Director</p>
    </div>

    <div class="contact-band"></div>
    <div class="divider"></div>

    <svg class="icons" viewBox="0 0 421 40" aria-hidden="true">
      <rect x="128" y="15" width="166" height="6" fill="#fff"/>
      <g fill="#00AB8E" stroke="#fff" stroke-width="3">
        <circle cx="152" cy="20" r="17"/>
        <circle cx="191" cy="20" r="17"/>
        <circle cx="230" cy="20" r="17"/>
        <circle cx="270" cy="20" r="17"/>
      </g>
      <g fill="none" stroke="#fff" stroke-width="1.8" stroke-linecap="round" stroke-linejoin="round">
        <path d="M147 11 l3 -1 l3 6 l-2 2 q1 4 5 7 l2 -2 l5 3 l-1 3 q-6 2 -12 -6 q-5 -7 -3 -12z"/>
        <rect x="183" y="14" width="16" height="12" rx="1.5"/>
        <path d="M183 15 l8 6 l8 -6"/>
        <circle cx="230" cy="20" r="8"/>
        <ellipse cx="230" cy="20" rx="3.5" ry="8"/>
        <path d="M222 20 h16 M223.5 16 h13 M223.5 24 h13"/>
        <path d="M270 29 q-7 -7 -7 -12 a7 7 0 0 1 14 0 q0 5 -7 12z"/>
        <circle cx="270" cy="17" r="2.3"/>
      </g>
    </svg>

    <div class="contact">
      <p>(07) 3555 0147</p>
      <p>brightlinktelco.com.au</p>
      <p>brightlinktelco.com.au</p>
      <p>Brisbane (head) office</p>
    </div>
  </section>

  <section class="card card--back">
    <div class="pattern" role="img" aria-label="Dark background with a repeating tone-on-tone brand pattern"></div>
    <p class="back-mark">Brightlink</p>
  </section>
</main>
</body>
</html>
```